Business Card Design

Marla Quibbet
Artist of Contemporary/Modern/Representational Art
Contact: 0457219308
Please include my web site (thanks)! http://www.artvault913.com.au/marla-quibbet
And
Email: marlaquibbet@fernpost.example

Target Market(s)

Modern professional People who know what they like in modern contemporary art and have the means to purchase it.

Industry/Entity Type

Business

Contact Information for Business Card

Marla Quibbet
Contact: 0457219308

Font styles to use
Sans Serif

Requirements
Must have
• Simplicity & to the point
Keep the font modern/ contemporary
Nice to have
• A portrait of me and one piece of work on the business card (one on each side).
Should not have
• I'm not into butterflies.
No feminine style swirls
Nor I like swirls that look like tatoos

```html
<!DOCTYPE html>
<html lang="en">
<head>
<meta charset="utf-8">
<title>Marla Quibbet — Business Card</title>
<link rel="stylesheet" href="https://fonts.googleapis.com/css2?family=Lobster&family=Lato:wght@300;400&display=swap">
<style>
  :root {
    --page: #e9e6e1;
    --navy: #1f1e5a;
    --band: #f1ece8;
    --ink-light: #ffffff;
    --art-silver: #d9d2c6;
    --art-pale: #efe9df;
    --art-grey: #8f8a86;
    --art-blue: #3b3f8a;
    --art-brown: #6b4a2c;
    --shadow: rgba(0,0,0,0.22);
  }
  * { margin: 0; padding: 0; box-sizing: border-box; }
  html, body { width: 1200px; height: 1023px; overflow: hidden; }
  body {
    background: var(--page);
    position: relative;
    font-family: "Lato", sans-serif;
  }
  .card {
    position: absolute;
    left: 250px;
    width: 700px;
    height: 420px;
    box-shadow: 0 8px 24px var(--shadow);
    overflow: hidden;
  }
  .card--front { top: 60px; }
  .card--back { top: 543px; background: var(--navy); color: var(--ink-light); }

  .artwork {
    position: absolute; inset: 0;
    background:
      radial-gradient(ellipse 16% 22% at 44% 62%, var(--art-brown) 0%, rgba(107,74,44,0) 100%),
      radial-gradient(ellipse 70% 55% at 55% 25%, var(--art-pale) 0%, var(--art-silver) 45%, rgba(143,138,134,0.6) 80%),
      linear-gradient(180deg, var(--art-silver) 0%, var(--art-grey) 55%, var(--art-blue) 100%);
  }
  .name-band {
    position: absolute;
    left: 0; right: 0;
    top: 262px;
    height: 92px;
    background: var(--band);
    display: flex;
    align-items: center;
    justify-content: center;
  }
  .name-band .card-name {
    font-family: "Lobster", cursive;
    font-size: 58px;
    color: var(--navy);
    letter-spacing: 1px;
  }

  .back-content {
    position: absolute;
    left: 70px; top: 62px;
  }
  .back-content .card-name {
    font-family: "Lobster", cursive;
    font-size: 64px;
    line-height: 1;
    color: var(--ink-light);
  }
  .tagline {
    margin-top: 18px;
    font-size: 19px;
    font-weight: 300;
    letter-spacing: 0.3px;
  }
  .contact { list-style: none; margin-top: 38px; }
  .contact li {
    display: flex; align-items: center; gap: 12px;
    font-size: 22px; font-weight: 400;
    margin-bottom: 26px;
  }
  .contact svg { flex: none; }
</style>
</head>
<body>
  <section class="card card--front">
    <div class="artwork" role="img" aria-label="Painting by the artist: pale silvery tangled branches over blue-shadowed tree trunks with a warm brown form"></div>
    <div class="name-band"><span class="card-name">Marla Quibbet</span></div>
  </section>

  <section class="card card--back">
    <div class="back-content">
      <h1 class="card-name">Marla Quibbet</h1>
      <p class="tagline">Artist of Contemporary | Modern | Representational Art</p>
      <ul class="contact">
        <li>
          <svg width="20" height="28" viewBox="0 0 20 28" aria-hidden="true">
            <rect x="2" y="1.5" width="16" height="25" rx="3" fill="none" stroke="#fff" stroke-width="2"/>
            <line x1="7" y1="22" x2="13" y2="22" stroke="#fff" stroke-width="2"/>
          </svg>
          <span>0457219308</span>
        </li>
        <li>
          <svg width="20" height="20" viewBox="0 0 20 20" aria-hidden="true">
            <circle cx="10" cy="10" r="8.5" fill="none" stroke="#fff" stroke-width="1.8"/>
            <ellipse cx="10" cy="10" rx="3.8" ry="8.5" fill="none" stroke="#fff" stroke-width="1.4"/>
            <line x1="1.5" y1="10" x2="18.5" y2="10" stroke="#fff" stroke-width="1.4"/>
          </svg>
          <span>www.artvault913.com.au/marla-quibbet</span>
        </li>
      </ul>
    </div>
  </section>
</body>
</html>
```